Beer Can Label design - HAZY NEIPA

Hazy NEIPA. (Acronym for New England India Pale Ale)
Full sleeve (473ml)
5.00" x 8.125" Inches
Write up on can reverse.
Opaque haze in appearance derived from specific oats, wheat, and water chemistry. This brew bolsters a dense and creamy head, leaving behind a soft and silky mouth-feel. Expect an intense tropical fruit centric aroma and flavour. Our timely hop additions contributes to less bitterness than typical IPA’s.
Logo is to be on front, towards bottom. Title near top.
Looking for something that stands out. Bold.
Target Market(s)
Craft beer enthusiasts
Industry/Entity Type
Beer & Brewing
Requirements
Must have
- Eye catching.

```html
<!DOCTYPE html>
<html lang="en">
<head>
<meta charset="utf-8">
<title>Hazy NEIPA – Can Label</title>
<link href="https://fonts.googleapis.com/css2?family=Smokum&family=Oswald:wght@500&family=Changa:wght@400&display=swap" rel="stylesheet">
<style>
  :root {
    --canvas-bg: #ffffff;
    --label-green: #5a9a2e;
    --leaf-tint: rgba(140, 200, 90, 0.28);
    --cream: #fdf3e3;
    --title-orange: #f3a659;
    --title-light: #fcefdc;
    --white: #ffffff;
  }
  * { margin: 0; padding: 0; box-sizing: border-box; }
  html, body {
    width: 1200px;
    height: 1000px;
    overflow: hidden;
    background: var(--canvas-bg);
  }
  .canvas {
    position: relative;
    width: 1200px;
    height: 1000px;
    background: var(--canvas-bg);
  }
  .label {
    position: absolute;
    left: 367px;
    top: 0;
    width: 466px;
    height: 1000px;
    background: var(--label-green);
    overflow: hidden;
    text-align: center;
    color: var(--white);
  }
  .leaf-pattern {
    position: absolute;
    width: 220px;
    height: 220px;
    border-radius: 50%;
    background: radial-gradient(circle, var(--leaf-tint) 0%, rgba(140,200,90,0) 70%);
  }
  .leaf-pattern--top-left { left: -90px; top: -70px; }
  .leaf-pattern--top-right { right: -90px; top: -60px; }
  .leaf-pattern--mid-left { left: -120px; top: 200px; }
  .leaf-pattern--mid-right { right: -120px; top: 210px; }
  .leaf-pattern--bottom-left { left: -90px; bottom: -60px; }
  .leaf-pattern--bottom-right { right: -90px; bottom: -60px; }

  .tagline {
    position: absolute;
    top: 104px;
    left: 0;
    width: 100%;
    font-family: 'Oswald', sans-serif;
    font-weight: 500;
    font-size: 34px;
    line-height: 44px;
    letter-spacing: 1px;
    color: var(--cream);
    white-space: nowrap;
  }
  .title {
    position: absolute;
    top: 152px;
    left: 40px;
    width: 386px;
    font-family: 'Smokum', 'Oswald', sans-serif;
    font-weight: 400;
    font-size: 170px;
    line-height: 164px;
    letter-spacing: 2px;
    white-space: nowrap;
    background: linear-gradient(180deg, var(--title-orange) 0%, var(--title-light) 100%);
    -webkit-background-clip: text;
    background-clip: text;
    color: transparent;
  }
  .title span { display: block; }
  .description {
    position: absolute;
    top: 506px;
    left: 63px;
    width: 340px;
    font-family: 'Changa', sans-serif;
    font-weight: 400;
    font-size: 15px;
    line-height: 24.5px;
    color: var(--white);
  }
  .brand {
    position: absolute;
    left: 120px;
    top: 700px;
    width: 226px;
    height: 226px;
    border: 7px solid var(--white);
    border-radius: 50%;
    display: flex;
    align-items: center;
    justify-content: center;
  }
  .brand-name {
    font-family: 'Oswald', sans-serif;
    font-weight: 500;
    font-size: 28px;
    line-height: 34px;
    color: var(--white);
    text-transform: uppercase;
  }
  .volume {
    position: absolute;
    bottom: 18px;
    left: 0;
    width: 100%;
    font-family: 'Oswald', sans-serif;
    font-weight: 500;
    font-size: 24px;
    line-height: 32px;
    color: var(--white);
  }
</style>
</head>
<body>
<main class="canvas">
  <section class="label">
    <div class="leaf-pattern leaf-pattern--top-left" role="img" aria-label="Faint hop leaf pattern"></div>
    <div class="leaf-pattern leaf-pattern--top-right" role="img" aria-label="Faint hop leaf pattern"></div>
    <div class="leaf-pattern leaf-pattern--mid-left" role="img" aria-label="Faint hop leaf pattern"></div>
    <div class="leaf-pattern leaf-pattern--mid-right" role="img" aria-label="Faint hop leaf pattern"></div>
    <div class="leaf-pattern leaf-pattern--bottom-left" role="img" aria-label="Faint hop leaf pattern"></div>
    <div class="leaf-pattern leaf-pattern--bottom-right" role="img" aria-label="Faint hop leaf pattern"></div>

    <p class="tagline">FOR THE HOP HEADS!</p>
    <h1 class="title"><span>HAZY</span><span>NEIPA</span></h1>
    <p class="description">Opaque haze in appearance derived from specific oats, wheat, and water chemistry. This brew bolsters a dense and creamy head, leaving behind a soft and silky mouth-feel. Expect an intense tropical fruit centric aroma and flavour. Our timely hop additions contributes to less bitterness than typical IPA’s.</p>

    <div class="brand">
      <p class="brand-name">Harbor Crown<br>Brew House</p>
    </div>

    <p class="volume">473 ml</p>
  </section>
</main>
</body>
</html>
```